Business card for a new innovative and professional lawn care business

We need a business card design for a new lawn care business in Halifax NS Canada. We offer lawn services in Halifax & Bedford. Our services offered include lawn care, garden services, and property maintenance. We take pride in our work and are experienced at what we do. I would like to see a design that is double sided. On the backside I would like the something simple (maybe my logo preferably on blackround (linked below) with website link, Facebook page or something). The front I want to include contact info:
Darren Maple
phone 902-555-0148
email - darrensyardworks.ca
facebook - Facebook.com/darrensyardworks
Instagram maybe ? - instagram.com/darrenyardworks
Serving Halifax and Bedford for 5 years?
I don't want it to have too much information as I will be passing them out in aim to visit website, or call !
We do want it to include lawn care, garden services and property maintenance.
Basic, catchy, and modern looking !
Logo attached below !

Target Market(s)

Passing business cards to everyone I meet or interact with.

Industry/Entity Type

Lawn Care

Contact Information for Business Card

Double sided with some basic information, with catchy colours and easy to look at.

Font styles to use
Sans Serif

Requirements
Must have
• Must be double sided and have :
• Name, Phone, Email, FB, Website, and 3 main services offered - lawn care, property maintenance, garden services
Nice to have
• Would be nice to have instagram link if it goes well on there
Should not have
• Don't want too much writing or images that are distracting

```html
<!DOCTYPE html>
<html lang="en">
<head>
<meta charset="utf-8">
<title>Darren's Yardworks – Business Card</title>
<link rel="stylesheet" href="https://fonts.googleapis.com/css2?family=Source+Sans+3:wght@400;600;700&display=swap">
<style>
  :root {
    --backdrop: #3f3936;
    --card: #141414;
    --card-edge: #0a0a0a;
    --green: #1f9a4a;
    --green-bright: #7ed321;
    --text-light: #e8e8e8;
    --divider: #8a8a8a;
  }
  * { box-sizing: border-box; margin: 0; padding: 0; }
  html, body {
    width: 1200px; height: 814px; overflow: hidden;
    background: var(--backdrop);
    font-family: "Source Sans 3", sans-serif;
  }
  .sheet {
    width: 1200px; height: 814px;
    display: flex; align-items: center; justify-content: center; gap: 48px;
  }
  .card {
    width: 540px; height: 310px;
    background: var(--card);
    border: 1px solid var(--card-edge);
    box-shadow: 0 12px 28px rgba(0,0,0,.45);
    position: relative;
    overflow: hidden;
  }
  /* Contact side */
  .card--contact { display: flex; align-items: center; }
  .mower-art {
    width: 190px; height: 210px;
    margin-left: 56px;
    background: linear-gradient(160deg, #1f9a4a, #12703a);
    border-radius: 8px;
  }
  .divider {
    width: 1px; height: 170px;
    background: var(--divider);
    margin: 0 26px 0 44px;
  }
  .contact-name {
    color: var(--green);
    font-weight: 600; font-size: 19px;
    margin-bottom: 8px;
  }
  .contact-list { list-style: none; }
  .contact-list li {
    display: flex; align-items: center; gap: 9px;
    color: var(--text-light);
    font-size: 14.5px; line-height: 22px;
    white-space: nowrap;
  }
  .contact-icon { width: 13px; height: 13px; flex: none; }
  /* Brand side */
  .card--brand {
    display: flex; flex-direction: column; align-items: center; justify-content: center;
    padding: 0 24px;
  }
  .brand-mark { display: flex; align-items: center; gap: 12px; }
  .brand-dot {
    width: 34px; height: 34px; border-radius: 50%;
    background: var(--green); flex: none;
  }
  .brand-name {
    color: var(--green);
    font-weight: 700; font-size: 36px; letter-spacing: 1px;
    text-transform: uppercase; line-height: 1;
    white-space: nowrap;
  }
  .services {
    margin-top: 48px;
    display: flex; align-items: center; gap: 6px;
    color: var(--text-light); font-size: 14px;
    white-space: nowrap;
  }
  .tick { width: 13px; height: 13px; flex: none; }
</style>
</head>
<body>
<main class="sheet">
  <section class="card card--contact">
    <div class="mower-art" role="img" aria-label="Green silhouette illustration of a push lawn mower"></div>
    <div class="divider"></div>
    <div class="contact">
      <p class="contact-name">Darren Maple</p>
      <ul class="contact-list">
        <li>
          <svg class="contact-icon" viewBox="0 0 16 16"><path fill="#1f9a4a" d="M3.5 1l2.5 3-1.5 1.8c.8 1.9 2.2 3.3 4.2 4.2L10.5 8.5l3 2.5-1.5 3C6 14 2 10 2 3z"/></svg>
          902-555-0148
        </li>
        <li>
          <svg class="contact-icon" viewBox="0 0 16 16"><rect x="1" y="3" width="14" height="10" fill="#1f9a4a"/><path d="M1 3l7 6 7-6" fill="none" stroke="#141414" stroke-width="1.4"/></svg>
          info@darrensyardworks.ca
        </li>
        <li>
          <svg class="contact-icon" viewBox="0 0 16 16"><circle cx="8" cy="8" r="7" fill="#1f9a4a"/></svg>
          darrensyardworks
        </li>
        <li>
          <svg class="contact-icon" viewBox="0 0 16 16"><rect x="1" y="1" width="14" height="14" rx="2" fill="#1f9a4a"/></svg>
          darrensyardworks
        </li>
        <li>
          <svg class="contact-icon" viewBox="0 0 16 16"><rect x="1" y="1" width="14" height="14" rx="2" fill="#1f9a4a"/></svg>
          darrenyardworks
        </li>
      </ul>
    </div>
  </section>

  <section class="card card--brand">
    <div class="brand-mark">
      <span class="brand-dot"></span>
      <span class="brand-name">Darren's Yardworks</span>
    </div>
    <p class="services">
      <span>Lawn Care</span>
      <svg class="tick" viewBox="0 0 16 16"><path d="M2 8.5l4 4L14 3.5" fill="none" stroke="#7ed321" stroke-width="2.6" stroke-linecap="round" stroke-linejoin="round"/></svg>
      <span>Property Maintenance</span>
      <svg class="tick" viewBox="0 0 16 16"><path d="M2 8.5l4 4L14 3.5" fill="none" stroke="#7ed321" stroke-width="2.6" stroke-linecap="round" stroke-linejoin="round"/></svg>
      <span>Garden Services</span>
    </p>
  </section>
</main>
</body>
</html>
```